Anzeigengestaltung für Brötchen- und Brotlieferant
Zielgruppe
Wir beliefern Privatkunden Freitag, Samstag und Sonntag mit Brötchen / Broten und suchen ein Design für eine Werbekampagne zur Neukundengewinnung über Facebook. Sprich ein Bild indem alles kurz und knapp für den Kunden erklärt wird und man damit Werbung schalten kann.

```html
<!DOCTYPE html>
<html lang="de">
<head>
<meta charset="utf-8">
<title>Brötchenservice Tobias Koppner – Anzeige</title>
<link href="https://fonts.googleapis.com/css2?family=Open+Sans:wght@400;700&display=swap" rel="stylesheet">
<style>
  :root {
    --bg: #e8e6e2;
    --brown: #5e4b3f;
    --brown-deep: #776656;
    --bread-crust: #a9743f;
    --bread-crumb: #cdb9a0;
    --bagel: #8a5e3e;
    --board: #6b4a33;
  }
  * { margin: 0; padding: 0; box-sizing: border-box; }
  html, body { width: 1200px; height: 629px; overflow: hidden; background: var(--bg); }
  .ad {
    position: relative; width: 1200px; height: 629px; overflow: hidden;
    background: var(--bg); font-family: "Open Sans", Arial, sans-serif; color: var(--brown);
  }
  .brand {
    position: absolute; left: 98px; top: 40px; width: 320px; text-align: center;
  }
  .brand-name {
    font-size: 31px; font-weight: 400; letter-spacing: 1px; line-height: 1.2; color: var(--brown);
  }
  .brand-mark {
    width: 150px; height: 150px; margin: 18px auto; border-radius: 50%;
    border: 3px solid var(--brown);
  }
  .headline {
    position: absolute; left: 75px; top: 338px;
    font-size: 40px; font-weight: 700; line-height: 53px;
  }
  .subline {
    position: absolute; left: 75px; top: 454px;
    font-size: 21px; line-height: 30px;
  }
  .facts {
    position: absolute; left: 70px; top: 544px; display: flex; align-items: center; gap: 20px;
    font-size: 16px;
  }
  .fact { display: flex; align-items: center; gap: 8px; }
  .fact svg { display: block; }
  .visual { position: absolute; left: 0; top: 0; }
</style>
</head>
<body>
<main class="ad">
  <svg class="visual" width="1200" height="629" viewBox="0 0 1200 629">
    <circle cx="1240" cy="660" r="310" fill="var(--brown-deep)"/>

    <!-- Leaf: round loaf -->
    <path d="M615 112 Q870 70 905 345 Q650 370 615 112 Z" fill="none" stroke="var(--brown-deep)" stroke-width="3"/>
    <path role="img" aria-label="Foto eines frisch gebackenen runden Brotlaibs"
          d="M632 126 Q852 96 886 330 Q665 350 632 126 Z" fill="var(--bread-crust)"/>

    <!-- Leaf: stacked bagels -->
    <path d="M905 8 Q980 120 905 240 Q830 120 905 8 Z" fill="none" stroke="var(--brown-deep)" stroke-width="3"/>
    <path role="img" aria-label="Foto eines Stapels Bagels auf einem Teller"
          d="M905 26 Q965 120 905 222 Q845 120 905 26 Z" fill="var(--bagel)"/>

    <!-- Leaf: sliced baguette -->
    <path d="M898 412 Q880 150 1198 140 Q1210 400 898 412 Z" fill="none" stroke="var(--brown-deep)" stroke-width="3"/>
    <path role="img" aria-label="Foto eines in Scheiben geschnittenen Baguettes auf einem Holzbrett"
          d="M914 398 Q900 170 1182 156 Q1190 385 914 398 Z" fill="var(--board)"/>

    <!-- Leaf: bread held in hands -->
    <path d="M555 338 Q900 320 935 629 L640 629 Q560 520 555 338 Z" fill="none" stroke="var(--brown-deep)" stroke-width="3"/>
    <path role="img" aria-label="Foto von Händen, die ein aufgeschnittenes Sauerteigbrot halten"
          d="M572 352 Q885 338 916 629 L655 629 Q578 515 572 352 Z" fill="var(--bread-crumb)"/>
  </svg>

  <header class="brand">
    <p class="brand-name">Brötchenservice</p>
    <div class="brand-mark"></div>
    <p class="brand-name">Tobias Koppner</p>
  </header>

  <h1 class="headline">Kein Brot zuhause?<br>Kein Problem!</h1>
  <p class="subline">Wir liefern Ihnen frisches Brot &amp; Brötchen<br>nach Hause!</p>

  <div class="facts">
    <span class="fact">
      <svg width="28" height="28" viewBox="0 0 28 28" aria-hidden="true">
        <circle cx="14" cy="14" r="12.5" fill="none" stroke="var(--brown)" stroke-width="2"/>
        <path d="M14 7 V14 H20" fill="none" stroke="var(--brown)" stroke-width="2" stroke-linecap="round"/>
      </svg>
      Freitags, Samstags &amp; Sonntags
    </span>
    <span class="fact">
      <svg width="22" height="30" viewBox="0 0 22 30" aria-hidden="true">
        <path d="M11 1 C5 1 1 5.5 1 11 C1 18 11 29 11 29 C11 29 21 18 21 11 C21 5.5 17 1 11 1 Z" fill="var(--brown)"/>
        <circle cx="11" cy="11" r="4" fill="var(--bg)"/>
      </svg>
      11111 Musterstadt
    </span>
  </div>
</main>
</body>
</html>
```